Business Card for a Renewable energy construction company

I need a formal, neat looking business card. Minimal and professional looking. Back side can have a design that is semi-ransparent/shaded

Target Market(s)

Renewable energy companies

Contact Information for Business Card

Name, Surname and contact details (phone, email)

Colors
00AB8E
00BBA5
67D7C9
C6EFE9
E9F9F6

Requirements
Must have
• Place for a QR code in the back side

```html
<!DOCTYPE html>
<html lang="en">
<head>
<meta charset="utf-8">
<title>Halvern Business Card</title>
<link rel="stylesheet" href="https://fonts.googleapis.com/css2?family=Poppins:wght@300;400;600;700&family=Open+Sans:wght@700&family=Roboto:wght@400&display=swap">
<style>
  :root {
    --page: #d8d4ce;
    --card-top: #f4f5f5;
    --card-bottom: #e3e6e6;
    --ink: #1b1e20;
    --band-dark: #17191b;
    --teal-deep: #14514f;
    --teal: #1f6e6d;
    --name-teal: #3c8a86;
    --text-light: #e8eeee;
    --icon-fill: #d8c8c0;
  }
  * { margin: 0; padding: 0; box-sizing: border-box; }
  html, body { width: 1200px; height: 970px; overflow: hidden; }
  body { background: var(--page); position: relative; }

  .card {
    position: absolute;
    left: 100px; top: 199px;
    width: 1000px; height: 572px;
    background: linear-gradient(180deg, var(--card-top), var(--card-bottom));
    overflow: hidden;
    box-shadow: 0 10px 30px rgba(0,0,0,0.18);
  }

  .brand {
    position: absolute;
    left: 160px; top: 86px;
    display: flex; align-items: center; gap: 18px;
  }
  .brand-square { width: 56px; height: 56px; background: var(--teal); }
  .brand-name {
    font-family: 'Poppins', sans-serif;
    font-weight: 700;
    font-size: 78px;
    line-height: 1;
    letter-spacing: 3px;
    color: var(--ink);
  }
  .tagline {
    position: absolute;
    left: 232px; top: 164px;
    font-family: 'Open Sans', sans-serif;
    font-weight: 700;
    font-size: 17px;
    letter-spacing: 2.3px;
    white-space: nowrap;
    color: var(--ink);
  }

  .contact-band {
    position: absolute;
    left: 0; top: 327px;
    width: 1000px; height: 201px;
    background: linear-gradient(90deg, var(--teal) 0%, var(--teal-deep) 70%, var(--teal) 100%);
  }
  .title-band {
    position: absolute;
    left: 0; top: 262px;
    width: 620px; height: 65px;
    background: linear-gradient(90deg, #2a2d2f, var(--band-dark));
    clip-path: polygon(0 0, 94% 0, 100% 100%, 0 100%);
  }
  .person {
    position: absolute;
    left: 58px; top: 275px;
    font-family: 'Poppins', sans-serif;
    font-size: 31px;
    line-height: 40px;
    white-space: nowrap;
  }
  .person-name { font-weight: 600; color: var(--name-teal); }
  .person-role { font-weight: 300; font-size: 27px; color: var(--text-light); }

  .address {
    position: absolute;
    left: 58px; top: 340px;
    font-family: 'Roboto', sans-serif;
    font-size: 23px;
    line-height: 32px;
    color: var(--text-light);
  }
  .details {
    position: absolute;
    left: 58px; top: 420px;
    list-style: none;
    font-family: 'Poppins', sans-serif;
    font-weight: 300;
    font-size: 24px;
    line-height: 33px;
    color: var(--text-light);
  }
  .details li { display: flex; align-items: center; gap: 10px; }
  .details svg { width: 24px; height: 24px; flex: none; }
</style>
</head>
<body>
  <main class="card">
    <div class="brand">
      <span class="brand-square"></span>
      <span class="brand-name">HALVERN</span>
    </div>
    <p class="tagline">ENGINEERING A GREENER TOMORROW</p>

    <div class="contact-band"></div>
    <div class="title-band"></div>
    <p class="person"><span class="person-name">NOAH R. BELLAMY</span> <span class="person-role">| Director</span></p>

    <p class="address">PO BOX 418 Larchmont Yard<br>7th street Denham, USA</p>

    <ul class="details">
      <li>
        <svg viewBox="0 0 24 24" aria-hidden="true">
          <circle cx="12" cy="12" r="12" fill="var(--icon-fill)"/>
          <path d="M8.5 6.5c.6-.4 1.2-.3 1.5.2l1 1.7c.3.5.2 1-.2 1.3l-.8.6c.5 1.3 1.5 2.5 2.8 3.2l.7-.7c.4-.4.9-.4 1.300-.1l1.6 1.1c.5.3.6 1 .2 1.5l-.8.9c-.6.6-1.5.8-2.300.4-2.900-1.300-5-3.600-6-6.500-.3-.8 0-1.700.6-2.200z" fill="var(--teal-deep)"/>
        </svg>
        <span>555-204-3178</span>
      </li>
      <li>
        <svg viewBox="0 0 24 24" aria-hidden="true">
          <circle cx="12" cy="12" r="12" fill="var(--icon-fill)"/>
          <rect x="6.5" y="8" width="11" height="8" rx="1" fill="var(--teal-deep)"/>
          <path d="M6.8 8.5l5.2 4 5.2-4" stroke="var(--icon-fill)" stroke-width="1.1" fill="none"/>
        </svg>
        <span>hello@halvernpower.com</span>
      </li>
    </ul>
  </main>
</body>
</html>
```